Business card design needed

Our modern electrical contracting company requires business card design utilising our logo and incorporating our tag line "Service when you need it". We specialise in assisting our customers 24/7 offering a breakdown service.

Industry/Entity Type

Electrical

Contact Information for Business Card

Marcus Penhale, Electrical contractor,Tel: (08) 8456 3071, Fax: (08) 8679 4315, Mob 0438 562 740, Email: marcus.penhale@brightwirepower.com.au, Web: www.brightwirepower.com.au

Requirements
Must have
• we require a 2 sided card.
Front- Logo, tag line and contact information.
Rear- service when you need it! Call now for our 24/7 breakdown service

```html
<!DOCTYPE html>
<html lang="en">
<head>
<meta charset="utf-8">
<title>Brightwire Power – Business Card Draft 1</title>
<link rel="stylesheet" href="https://fonts.googleapis.com/css2?family=Arimo:wght@400;700&family=Oswald:wght@500;700&display=swap">
<style>
  :root {
    --paper: #ffffff;
    --ink: #222222;
    --card-blue: #3b73c2;
    --navy: #1d3c85;
    --cyan: #1ea9e9;
    --brand-blue: #2552a6;
    --black: #050505;
    --sky-text: #2ba6e3;
    --white: #ffffff;
  }
  html, body {
    margin: 0;
    width: 1200px;
    height: 812px;
    overflow: hidden;
    background: var(--paper);
  }
  .sheet {
    position: relative;
    width: 1200px;
    height: 812px;
    font-family: "Arimo", Arial, sans-serif;
  }
  .job-label {
    position: absolute;
    left: 50px;
    top: 18px;
    margin: 0;
    font-size: 12.5px;
    line-height: 15px;
    color: var(--ink);
  }
  .card {
    position: absolute;
    width: 348px;
    height: 198px;
    filter: drop-shadow(2px 3px 3px rgba(0,0,0,0.35));
  }
  .card svg { display: block; }
  .front-1 { left: 50px;  top: 136px; }
  .front-2 { left: 427px; top: 136px; }
  .front-3 { left: 802px; top: 136px; }
  .back-1  { left: 50px;  top: 416px; }
  .back-2  { left: 427px; top: 416px; }
  .back-3  { left: 802px; top: 416px; }

  .sans { font-family: "Arimo", Arial, sans-serif; }
  .display { font-family: "Oswald", "Arial Narrow", sans-serif; font-weight: 700; }
  .brand-name { font-family: "Oswald", "Arial Narrow", sans-serif; font-weight: 700; fill: var(--brand-blue); }

  .footer-brand {
    position: absolute;
    left: 980px;
    top: 724px;
    width: 180px;
    text-align: center;
  }
  .footer-brand .brand-dot {
    display: block;
    width: 46px;
    height: 46px;
    margin: 0 auto 6px;
    border-radius: 50%;
    background: var(--brand-blue);
  }
  .footer-brand .brand-text {
    font-family: "Oswald", "Arial Narrow", sans-serif;
    font-weight: 700;
    font-size: 17px;
    letter-spacing: 0.3px;
    color: var(--brand-blue);
  }
</style>
</head>
<body>
<main class="sheet">
  <p class="job-label">BUSINESS CARD<br>Draft 1 - 130120<br>Job 83489</p>

  <!-- Front option 1 -->
  <div class="card front-1">
    <svg width="348" height="198" viewBox="0 0 348 198">
      <rect width="348" height="198" fill="var(--card-blue)"/>
      <path d="M0 0 H150 C205 60 200 150 165 198 H0 Z" fill="var(--cyan)"/>
      <path d="M0 0 H140 C190 60 186 150 155 198 H0 Z" fill="var(--navy)"/>
      <path d="M0 0 H96 C162 55 170 150 140 198 H0 Z" fill="var(--white)"/>
      <rect x="284" y="0" width="64" height="41" fill="var(--navy)"/>
      <text x="316" y="21" class="sans" font-size="14" fill="var(--white)" text-anchor="middle">24/7</text>
      <text x="316" y="33" class="sans" font-size="9" fill="var(--white)" text-anchor="middle">service</text>
      <circle cx="65" cy="58" r="40" fill="var(--brand-blue)"/>
      <text x="10" y="144" class="brand-name" font-size="12.5">BRIGHTWIRE POWER</text>
      <text x="12" y="155" class="sans" font-size="7.5" fill="var(--brand-blue)">www.brightwirepower.com.au</text>
      <text x="207" y="89" class="sans" font-size="15" fill="var(--white)" textLength="130" lengthAdjust="spacingAndGlyphs">MARCUS PENHALE</text>
      <text x="207" y="101" class="sans" font-size="9.5" fill="var(--white)">electrical contractor</text>
      <text x="207" y="117" class="sans" font-size="13" fill="var(--white)">0438 562 740</text>
      <text x="168" y="179" class="sans" font-size="7.6" fill="var(--white)">P: (08) 8456 3071   |   F: (08) 8679 4315</text>
      <text x="168" y="191" class="sans" font-size="7.6" fill="var(--white)">E: marcus.penhale@brightwirepower.com.au</text>
    </svg>
  </div>

  <!-- Front option 2 -->
  <div class="card front-2">
    <svg width="348" height="198" viewBox="0 0 348 198">
      <rect width="348" height="198" fill="var(--card-blue)"/>
      <path d="M0 0 H140 C190 60 188 150 150 198 H0 Z" fill="var(--cyan)"/>
      <path d="M0 0 H128 C178 60 176 150 140 198 H0 Z" fill="var(--navy)"/>
      <path d="M0 0 H96 C162 55 168 150 132 198 H0 Z" fill="var(--white)"/>
      <path d="M258 0 H348 V41 H300 C288 28 274 12 258 0 Z" fill="var(--cyan)"/>
      <path d="M266 0 H348 V41 H306 C296 26 282 12 266 0 Z" fill="var(--navy)"/>
      <path d="M170 160 L348 160 V198 H150 Z" fill="var(--navy)"/>
      <text x="316" y="21" class="sans" font-size="14" fill="var(--white)" text-anchor="middle">24/7</text>
      <text x="316" y="33" class="sans" font-size="9" fill="var(--white)" text-anchor="middle">service</text>
      <circle cx="65" cy="58" r="40" fill="var(--brand-blue)"/>
      <text x="10" y="144" class="brand-name" font-size="12.5">BRIGHTWIRE POWER</text>
      <text x="12" y="155" class="sans" font-size="7.5" fill="var(--brand-blue)">www.brightwirepower.com.au</text>
      <text x="207" y="89" class="sans" font-size="15" fill="var(--white)" textLength="130" lengthAdjust="spacingAndGlyphs">MARCUS PENHALE</text>
      <text x="207" y="101" class="sans" font-size="9.5" fill="var(--white)">electrical contractor</text>
      <text x="207" y="117" class="sans" font-size="13" fill="var(--white)">0438 562 740</text>
      <text x="168" y="179" class="sans" font-size="7.6" fill="var(--white)">P: (08) 8456 3071   |   F: (08) 8679 4315</text>
      <text x="168" y="191" class="sans" font-size="7.6" fill="var(--white)">E: marcus.penhale@brightwirepower.com.au</text>
    </svg>
  </div>

  <!-- Front option 3 -->
  <div class="card front-3">
    <svg width="348" height="198" viewBox="0 0 348 198">
      <rect width="348" height="198" fill="var(--white)"/>
      <rect y="136" width="348" height="5" fill="var(--navy)"/>
      <rect y="141" width="348" height="57" fill="var(--card-blue)"/>
      <circle cx="41" cy="37" r="25" fill="var(--brand-blue)"/>
      <text x="74" y="49" class="brand-name" font-size="29">BRIGHTWIRE POWER</text>
      <text x="76" y="64" class="sans" font-size="9.5" letter-spacing="2.2" fill="var(--ink)">www.brightwirepower.com.au</text>
      <text x="128" y="89" class="sans" font-size="17" fill="var(--brand-blue)">MARCUS PENHALE</text>
      <text x="128" y="101" class="sans" font-size="9.5" fill="var(--brand-blue)">electrical contractor</text>
      <text x="128" y="116" class="sans" font-size="12.5" fill="var(--brand-blue)">0438 562 740</text>
      <text x="14" y="164" class="sans" font-size="9" fill="var(--white)">P : (08) 8456 3071</text>
      <text x="14" y="176" class="sans" font-size="9" fill="var(--white)">F : (08) 8679 4315</text>
      <text x="14" y="188" class="sans" font-size="9" fill="var(--white)">E : marcus.penhale@brightwirepower.com.au</text>
      <text x="336" y="175" class="sans" font-size="19" fill="var(--white)" text-anchor="end">24/7</text>
      <text x="336" y="187" class="sans" font-size="10" fill="var(--white)" text-anchor="end">service</text>
    </svg>
  </div>

  <!-- Back option 1 -->
  <div class="card back-1">
    <svg width="348" height="198" viewBox="0 0 348 198">
      <defs>
        <linearGradient id="back1-bg" x1="0" y1="0" x2="1" y2="0">
          <stop offset="0" stop-color="#2c57a8"/>
          <stop offset="0.45" stop-color="#13254f"/>
          <stop offset="0.6" stop-color="var(--black)"/>
        </linearGradient>
        <linearGradient id="mark-area" x1="0" y1="0" x2="0" y2="1">
          <stop offset="0" stop-color="#ffffff"/>
          <stop offset="1" stop-color="#d9e2f2"/>
        </linearGradient>
      </defs>
      <rect width="348" height="198" fill="url(#back1-bg)"/>
      <rect x="124" y="4" width="98" height="190" fill="url(#mark-area)" opacity="0.9" role="img" aria-label="Large brand mark area"/>
      <text x="12" y="34" class="display" font-size="24" fill="var(--white)">SERVICE</text>
      <text x="116" y="45" class="display" font-size="8.5" fill="var(--white)" text-anchor="end">WHEN YOU</text>
      <text x="10" y="70" class="display" font-size="22" fill="var(--white)">NEED IT!</text>
      <text x="336" y="132" class="display" font-size="25" fill="var(--white)" text-anchor="end">CALL NOW</text>
      <text x="268" y="160" class="display" font-size="9.5" fill="var(--white)" text-anchor="end">FOR OUR</text>
      <text x="336" y="168" class="display" font-size="32" fill="var(--white)" text-anchor="end">24/7</text>
      <text x="336" y="184" class="display" font-size="10.5" fill="var(--white)" text-anchor="end">BREAKDOWN SERVICE</text>
    </svg>
  </div>

  <!-- Back option 2 -->
  <div class="card back-2">
    <svg width="348" height="198" viewBox="0 0 348 198">
      <defs>
        <linearGradient id="back2-bg" x1="0" y1="0" x2="1" y2="0">
          <stop offset="0" stop-color="#2c57a8"/>
          <stop offset="0.4" stop-color="#13254f"/>
          <stop offset="0.55" stop-color="var(--black)"/>
        </linearGradient>
        <linearGradient id="mark-area-2" x1="0" y1="0" x2="0" y2="1">
          <stop offset="0" stop-color="#ffffff"/>
          <stop offset="1" stop-color="#d9e2f2"/>
        </linearGradient>
      </defs>
      <rect width="348" height="198" fill="url(#back2-bg)"/>
      <rect x="55" y="6" width="98" height="188" fill="url(#mark-area-2)" opacity="0.9" role="img" aria-label="Large brand mark area"/>
      <text x="334" y="46" class="display" font-size="31" fill="var(--white)" text-anchor="end">SERVICE</text>
      <text x="334" y="61" class="display" font-size="11" fill="var(--white)" text-anchor="end">when you NEED it!</text>
      <text x="178" y="146" class="display" font-size="29" fill="var(--white)">CALL NOW</text>
      <text x="178" y="169" class="display" font-size="20" fill="var(--white)">(08) 8456 3071</text>
      <text x="178" y="186" class="display" font-size="11" fill="var(--white)">24/7 BREAKDOWN SERVICE</text>
    </svg>
  </div>

  <!-- Back option 3 -->
  <div class="card back-3">
    <svg width="348" height="198" viewBox="0 0 348 198">
      <defs>
        <linearGradient id="back3-bg" x1="0" y1="0" x2="1" y2="0">
          <stop offset="0" stop-color="#2c57a8"/>
          <stop offset="0.55" stop-color="#13254f"/>
          <stop offset="0.75" stop-color="var(--black)"/>
        </linearGradient>
        <linearGradient id="mark-area-3" x1="0" y1="0" x2="0" y2="1">
          <stop offset="0" stop-color="#ffffff"/>
          <stop offset="1" stop-color="#d9e2f2"/>
        </linearGradient>
      </defs>
      <rect width="348" height="198" fill="url(#back3-bg)"/>
      <rect x="196" y="6" width="98" height="188" fill="url(#mark-area-3)" opacity="0.9" role="img" aria-label="Large brand mark area"/>
      <text x="16" y="48" class="display" font-size="33" fill="var(--sky-text)">SERVICE</text>
      <text x="166" y="61" class="display" font-size="11" fill="var(--sky-text)" text-anchor="end">when you NEED it!</text>
      <text x="16" y="146" class="display" font-size="30" fill="var(--sky-text)">CALL NOW</text>
      <text x="16" y="169" class="display" font-size="20" fill="var(--sky-text)">(08) 8456 3071</text>
      <text x="16" y="186" class="display" font-size="11" fill="var(--sky-text)">24/7 BREAKDOWN SERVICE</text>
    </svg>
  </div>

  <div class="footer-brand">
    <span class="brand-dot"></span>
    <span class="brand-text">BRIGHTWIRE POWER</span>
  </div>
</main>
</body>
</html>
```